Bref créative
BrightPath Fuel
Eye Catching Card & Letterhead Design
Professional
Marcus Torres
CEO
4183 HAWTHORNE AVE
SUITE 310
SARASOTA FL 34519
mtorres@brightpathfuel.example
www.brightpathfuel.example
use the WELL portion of the logo and list the twitter site (@brightpathfuel)

```html
<!DOCTYPE html>
<html lang="en">
<head>
<meta charset="utf-8">
<title>BrightPath Fuel — Business Card</title>
<link href="https://fonts.googleapis.com/css2?family=Open+Sans:wght@400;600;700&display=swap" rel="stylesheet">
<style>
  :root {
    --bg: #e9e6e1;
    --card: #ffffff;
    --green: #8cbf26;
    --green-dark: #6f9d14;
    --green-light: #a9d14a;
    --ink: #3a3a3a;
    --ink-soft: #6b6b6b;
    --black: #111111;
  }
  html, body {
    margin: 0;
    padding: 0;
    width: 1200px;
    height: 739px;
    overflow: hidden;
    background: var(--bg);
    font-family: "Open Sans", Arial, sans-serif;
  }
  .canvas {
    position: relative;
    width: 1200px;
    height: 739px;
  }
  .card {
    position: absolute;
    background: var(--card);
    box-shadow: 0 6px 18px rgba(0,0,0,0.18);
    overflow: hidden;
  }
  /* Back of card */
  .card-back {
    left: 50px;
    top: 215px;
    width: 520px;
    height: 297px;
  }
  .back-brand {
    position: absolute;
    left: 0;
    right: 0;
    top: 108px;
    display: flex;
    justify-content: center;
    align-items: center;
    gap: 10px;
  }
  .brand-dot {
    width: 16px;
    height: 16px;
    border-radius: 50%;
    background: var(--green);
    flex: none;
  }
  .brand-name {
    font-weight: 700;
    color: var(--green);
    letter-spacing: 0.5px;
    white-space: nowrap;
  }
  .back-brand .brand-name { font-size: 28px; }
  .back-web {
    position: absolute;
    left: 0;
    right: 0;
    top: 165px;
    text-align: center;
    font-size: 12px;
    font-weight: 600;
    color: var(--ink);
  }
  /* Front of card */
  .card-front {
    left: 620px;
    top: 215px;
    width: 540px;
    height: 309px;
  }
  .front-panel {
    position: absolute;
    inset: 0;
  }
  .holder {
    position: absolute;
    left: 410px;
    top: 62px;
    color: #ffffff;
  }
  .holder-name {
    font-size: 15px;
    font-weight: 700;
    margin: 0;
    white-space: nowrap;
  }
  .holder-title {
    font-size: 11px;
    font-weight: 400;
    margin: 2px 0 0;
    padding-left: 18px;
  }
  .front-brand {
    position: absolute;
    left: 34px;
    top: 118px;
    display: flex;
    align-items: center;
    gap: 10px;
  }
  .front-brand .brand-name { font-size: 30px; }
  .contact {
    position: absolute;
    left: 38px;
    top: 190px;
    font-size: 11px;
    line-height: 15px;
    color: var(--ink);
  }
  .contact p { margin: 0; white-space: nowrap; }
  .contact .address { margin-bottom: 6px; }
  .contact-line {
    display: flex;
    align-items: center;
    gap: 7px;
  }
  .contact-line svg { width: 10px; height: 10px; flex: none; }
</style>
</head>
<body>
<main class="canvas">

  <section class="card card-back" aria-label="Card back">
    <div class="back-brand">
      <span class="brand-dot"></span>
      <span class="brand-name">BrightPath Fuel</span>
    </div>
    <div class="back-web">www.brightpathfuel.example</div>
  </section>

  <section class="card card-front" aria-label="Card front">
    <svg class="front-panel" viewBox="0 0 540 309" width="540" height="309">
      <defs>
        <linearGradient id="panelGreen" x1="0" y1="0" x2="1" y2="1">
          <stop offset="0" stop-color="#a9d14a"/>
          <stop offset="1" stop-color="#6f9d14"/>
        </linearGradient>
      </defs>
      <path d="M336,0 Q296,200 540,296 L540,0 Z" fill="url(#panelGreen)" role="img" aria-label="Green panel with soft leaf texture"/>
      <path d="M336,0 Q296,200 540,296" fill="none" stroke="#111111" stroke-width="6"/>
    </svg>

    <div class="holder">
      <p class="holder-name">Marcus Torres</p>
      <p class="holder-title">CEO</p>
    </div>

    <div class="front-brand">
      <span class="brand-dot"></span>
      <span class="brand-name">BrightPath Fuel</span>
    </div>

    <div class="contact">
      <p class="address">4183 HAWTHORNE AVE Suite 310<br>Sarasota FL 34519</p>
      <p class="contact-line">
        <svg viewBox="0 0 10 10" aria-hidden="true"><path d="M2 1 L4 1 L4.6 3 L3.4 3.8 Q4.4 5.8 6.2 6.6 L7 5.4 L9 6 L9 8 Q5 9.5 1 3 Z" fill="#6b6b6b"/></svg>
        407 555 0182
      </p>
      <p class="contact-line">
        <svg viewBox="0 0 10 10" aria-hidden="true"><rect x="0.5" y="2" width="9" height="6" fill="none" stroke="#6b6b6b"/><path d="M0.5 2 L5 5.5 L9.5 2" fill="none" stroke="#6b6b6b"/></svg>
        mtorres@brightpathfuel.example
      </p>
      <p class="contact-line">
        <svg viewBox="0 0 10 10" aria-hidden="true"><circle cx="5" cy="5" r="4.3" fill="none" stroke="#6b6b6b"/><ellipse cx="5" cy="5" rx="1.8" ry="4.3" fill="none" stroke="#6b6b6b"/><path d="M0.7 5 H9.3" stroke="#6b6b6b"/></svg>
        www.brightpathfuel.example
      </p>
      <p class="contact-line">
        <svg viewBox="0 0 10 10" aria-hidden="true"><circle cx="5" cy="5" r="4.3" fill="#6b6b6b"/></svg>
        @brightpathfuel
      </p>
    </div>
  </section>

</main>
</body>
</html>
```